Cover Art Needed For Digital Single Release

We are looking to have the cover art designed for a new song called "Paper Lanterns". You will find the track attached below in a private TuneVault link so that you can have a listen.
We are thinking of keeping the artwork fairly simple but still want it to catch your eye. Maybe using the song title and artist’s name in a colorful and creative way. (A well-designed font with a bold color scheme, or even something like a mosaic style art piece featuring the title).
We completely welcome any and all creative visions you might have, even if it strays away from the examples given above.
Thank you in advance for your submissions, and we are excited to collaborate with you!
"Paper Lanterns" by Marcus Holloway
https://tunevault.example/marcusxyz/paper-lanterns/s-r7Tq2wLmNcx
Target Market(s)
Teens/Young Adults
Industry/Entity Type
Music
Requirements
Must have
- An eye-catching design
Should not have
- Please do not rely heavily on stock images. We prefer an original design/concept.

```html
<!DOCTYPE html>
<html lang="en">
<head>
<meta charset="utf-8">
<title>Paper Lanterns — Marcus Holloway</title>
<link rel="stylesheet" href="https://fonts.googleapis.com/css2?family=Anton&family=Raleway:wght@500&display=swap">
<style>
  :root {
    --red-deep: #c8103f;
    --red-hot: #ff2b5c;
    --violet-edge: #7a2c78;
    --cyan: #3fe6f2;
    --cyan-light: #7ff4f8;
    --cyan-shade: #2bb8e0;
    --mint: #d8fff2;
  }
  html, body {
    margin: 0;
    padding: 0;
    overflow: hidden;
    background: #ffffff;
  }
  .cover {
    position: relative;
    width: 1200px;
    height: 1200px;
    overflow: hidden;
  }
  .cover__art {
    position: absolute;
    inset: 0;
    display: block;
  }
  .cover__title {
    font-family: "Anton", "Oswald", sans-serif;
  }
  .cover__artist {
    font-family: "Raleway", "Montserrat", sans-serif;
    font-weight: 500;
    letter-spacing: 12px;
  }
</style>
</head>
<body>
<div class="cover">
  <svg class="cover__art" width="1200" height="1200" viewBox="0 0 1200 1200">
    <defs>
      <radialGradient id="backdrop-glow" cx="50%" cy="50%" r="75%">
        <stop offset="0%" stop-color="var(--red-hot)"/>
        <stop offset="55%" stop-color="var(--red-deep)"/>
        <stop offset="100%" stop-color="var(--violet-edge)"/>
      </radialGradient>
      <linearGradient id="title-fill" x1="0" y1="0" x2="0" y2="1">
        <stop offset="0%" stop-color="var(--cyan-light)"/>
        <stop offset="55%" stop-color="var(--cyan)"/>
        <stop offset="100%" stop-color="var(--cyan-shade)"/>
      </linearGradient>
    </defs>

    <rect class="backdrop" role="img" aria-label="Mirrored painted texture in hot red and violet with faint magenta brush strokes" x="0" y="0" width="1200" height="1200" fill="url(#backdrop-glow)"/>

    <rect class="frame" x="57" y="57" width="1086" height="1086" fill="none" stroke="var(--cyan)" stroke-width="5"/>

    <text class="cover__title cover__title--top" x="115" y="447" font-size="500" textLength="990" lengthAdjust="spacingAndGlyphs" fill="url(#title-fill)">PAPER</text>

    <text class="cover__artist" x="600" y="618" font-size="50" text-anchor="middle" fill="var(--mint)">MARCUS HOLLOWAY</text>

    <text class="cover__title cover__title--bottom" x="105" y="1097" font-size="500" textLength="1000" lengthAdjust="spacingAndGlyphs" fill="url(#title-fill)">LANTERNS</text>
  </svg>
</div>
</body>
</html>
```